Tor'k Wayfarer Travel

We need a sleek, professional, inviting card to elicit global travel for the experienced and professional traveler. Royal blue, black and silver. (perhaps the wording could be silver with black shadow?-get creative) Maybe a watermark on the front and the full raised logo on the back.
We want a stylish and modern card, but professional.

```html
<!DOCTYPE html>
<html lang="en">
<head>
<meta charset="utf-8">
<title>Tor'k Wayfarer Travel — Business Card</title>
<link rel="stylesheet" href="https://fonts.googleapis.com/css2?family=Montserrat:wght@500;600;700&family=Poppins:wght@400&display=swap">
<style>
  :root {
    --stage: #2a2a2c;
    --card: #0b0b0c;
    --royal: #4a6fd1;
    --silver: #e6e8ec;
    --white: #ffffff;
  }
  html, body {
    margin: 0;
    width: 1200px;
    height: 900px;
    overflow: hidden;
    background: var(--stage);
  }
  .canvas {
    position: relative;
    width: 1200px;
    height: 900px;
  }
  .card {
    position: absolute;
    left: 250px;
    width: 700px;
    height: 400px;
    background: var(--card);
    border-radius: 22px;
    box-shadow: 0 10px 28px rgba(0,0,0,.45);
    overflow: hidden;
  }
  .card--front { top: 35px; }
  .card--back { top: 465px; }

  .brand {
    display: flex;
    align-items: center;
    gap: 12px;
    font-family: "Montserrat", sans-serif;
    font-weight: 700;
    color: var(--royal);
    letter-spacing: .06em;
    text-transform: uppercase;
    white-space: nowrap;
  }
  .brand__dot {
    width: 14px;
    height: 14px;
    border-radius: 50%;
    background: var(--royal);
  }
  .card--front .brand {
    position: absolute;
    left: 50%;
    top: 50%;
    transform: translate(-50%, -50%);
    font-size: 34px;
  }
  .card--back .brand {
    position: absolute;
    left: 48px;
    top: 150px;
    font-size: 21px;
  }

  .owner {
    position: absolute;
    right: 54px;
    top: 52px;
    text-align: right;
    font-family: "Montserrat", sans-serif;
  }
  .owner__name {
    color: var(--white);
    font-weight: 700;
    font-size: 20px;
    letter-spacing: .04em;
    text-transform: uppercase;
  }
  .owner__role {
    color: var(--royal);
    font-weight: 500;
    font-size: 13px;
    letter-spacing: .05em;
    margin-top: 4px;
    text-transform: uppercase;
  }
  .owner__bar {
    display: inline-block;
    width: 46px;
    height: 4px;
    background: var(--royal);
    margin-top: 8px;
  }

  .flight-path {
    position: absolute;
    inset: 0;
  }
  .plane-mark {
    position: absolute;
    right: 54px;
    top: 148px;
    width: 74px;
    height: 44px;
    border-radius: 22px;
    background: radial-gradient(ellipse at center, #f2f3f5 0%, #c9ccd2 60%, rgba(11,11,12,0) 100%);
  }

  .contact {
    position: absolute;
    right: 48px;
    top: 218px;
    list-style: none;
    margin: 0;
    padding: 0;
    font-family: "Poppins", sans-serif;
    font-size: 15px;
    color: var(--silver);
    text-align: right;
  }
  .contact li {
    display: flex;
    justify-content: flex-end;
    align-items: center;
    gap: 10px;
    height: 30px;
  }
  .contact svg {
    width: 16px;
    height: 16px;
    fill: none;
    stroke: var(--royal);
    stroke-width: 2;
  }
</style>
</head>
<body>
<main class="canvas">

  <section class="card card--front" aria-label="Card front">
    <div class="brand"><span class="brand__dot"></span>Tor'k Wayfarer Travel</div>
  </section>

  <section class="card card--back" aria-label="Card back">
    <svg class="flight-path" viewBox="0 0 700 400" aria-hidden="true">
      <defs>
        <linearGradient id="trail" x1="0" y1="1" x2="1" y2="0">
          <stop offset="0" stop-color="#4a6fd1"/>
          <stop offset=".85" stop-color="#4a6fd1"/>
          <stop offset="1" stop-color="#4a6fd1" stop-opacity="0"/>
        </linearGradient>
      </defs>
      <polygon points="52,318 585,168 585,170 52,334" fill="url(#trail)"/>
    </svg>

    <div class="brand"><span class="brand__dot"></span>Tor'k Wayfarer Travel</div>

    <div class="owner">
      <div class="owner__name">Maren Oduya Finch</div>
      <div class="owner__role">CEO/Founder</div>
      <span class="owner__bar"></span>
    </div>

    <div class="plane-mark" role="img" aria-label="Silver airplane silhouette in flight"></div>

    <ul class="contact">
      <li>+1-555-014-0287
        <svg viewBox="0 0 24 24" aria-hidden="true"><path d="M5 3h4l2 5-2.5 1.5a11 11 0 0 0 6 6L16 13l5 2v4a2 2 0 0 1-2 2A16 16 0 0 1 3 5a2 2 0 0 1 2-2z"/></svg>
      </li>
      <li>maren@torkwayfarertravel.com
        <svg viewBox="0 0 24 24" aria-hidden="true"><rect x="3" y="5" width="18" height="14" rx="1"/><path d="M3 6l9 7 9-7"/></svg>
      </li>
      <li>torkwayfarertravel.com
        <svg viewBox="0 0 24 24" aria-hidden="true"><circle cx="12" cy="12" r="9"/><path d="M3 12h18M12 3a14 14 0 0 1 0 18M12 3a14 14 0 0 0 0 18"/></svg>
      </li>
    </ul>
  </section>

</main>
</body>
</html>
```